BrightCampusPicks blogger needs pagely book cover

The title for the book is "Mapping School Options: A Handbook for Reading Campus Pages to Spend Little on a Stronger Degree"

Title must legible for Pagely store. I only need to front, no back or spine. The cover should be optimized to display on Vornex. Image size should be 1880x2500.

This book isn’t about how to apply to college or which classes to take or how to score higher on the QRT. It’s only focus is on how to use college websites to create a better college list. This is part of my general approach for families to use information important to their situation to find affordable colleges. I've attached a file with some covers from the category I like. I'm pretty flexible regarding colors, fonts, etc.

Target Market(s)

Parents of high school students worried about paying for college.

Industry/Entity Type

College

Requirements
Must have
• Title must be legible at small size.

```html
<!DOCTYPE html>
<html lang="en">
<head>
<meta charset="utf-8">
<title>Mapping School Options – Book Cover</title>
<link rel="stylesheet" href="https://fonts.googleapis.com/css2?family=Graduate&family=Bebas+Neue&display=swap">
<style>
  :root {
    --paper: #ffffff;
    --ink: #111111;
    --blue: #1f6fc0;
    --gold: #f9c80e;
    --laptop-silver: #c9ccd1;
    --laptop-screen: #b8864e;
  }
  html, body {
    margin: 0;
    padding: 0;
    overflow: hidden;
    background: var(--paper);
  }
  .cover {
    position: relative;
    width: 800px;
    height: 1200px;
    overflow: hidden;
    background: var(--paper);
  }
  .cover-art {
    position: absolute;
    left: 139px;
    top: 0;
    width: 537px;
    height: 398px;
  }
  .title {
    position: absolute;
    top: 425px;
    left: 0;
    width: 800px;
    margin: 0;
    text-align: center;
    font-family: "Graduate", "Times New Roman", serif;
    font-weight: 400;
    line-height: 1;
  }
  .title-line {
    display: block;
    color: var(--ink);
    text-shadow:
      2px 0 0 var(--paper), -2px 0 0 var(--paper), 0 2px 0 var(--paper), 0 -2px 0 var(--paper),
      2px 2px 0 var(--paper), -2px -2px 0 var(--paper), 2px -2px 0 var(--paper), -2px 2px 0 var(--paper),
      4px 0 0 var(--ink), -4px 0 0 var(--ink), 0 4px 0 var(--ink), 0 -4px 0 var(--ink),
      4px 4px 0 var(--ink), -4px -4px 0 var(--ink), 4px -4px 0 var(--ink), -4px 4px 0 var(--ink);
  }
  .title-line--top {
    font-size: 100px;
    letter-spacing: 2px;
  }
  .title-line--accent {
    color: var(--blue);
    font-size: 128px;
    margin-top: 12px;
    text-shadow:
      2px 0 0 var(--paper), -2px 0 0 var(--paper), 0 2px 0 var(--paper), 0 -2px 0 var(--paper),
      2px 2px 0 var(--paper), -2px -2px 0 var(--paper), 2px -2px 0 var(--paper), -2px 2px 0 var(--paper),
      4px 0 0 var(--blue), -4px 0 0 var(--blue), 0 4px 0 var(--blue), 0 -4px 0 var(--blue),
      4px 4px 0 var(--blue), -4px -4px 0 var(--blue), 4px -4px 0 var(--blue), -4px 4px 0 var(--blue);
  }
  .title-line--bottom {
    font-size: 100px;
    letter-spacing: 2px;
    margin-top: 16px;
  }
  .subtitle-band {
    position: absolute;
    left: 0;
    top: 861px;
    width: 800px;
    height: 250px;
    background: var(--gold);
    display: flex;
    flex-direction: column;
    justify-content: center;
    align-items: center;
  }
  .subtitle {
    margin: 0;
    font-family: "Bebas Neue", "Arial Narrow", sans-serif;
    font-weight: 400;
    color: var(--ink);
    line-height: 1.02;
    text-align: center;
  }
  .subtitle-line { display: block; }
  .subtitle-line--one { font-size: 56px; letter-spacing: 1px; }
  .subtitle-line--two { font-size: 72px; letter-spacing: 1px; }
  .subtitle-line--three { font-size: 50px; letter-spacing: 1px; }
</style>
</head>
<body>
  <main class="cover">
    <svg class="cover-art" viewBox="0 0 537 398" role="img" aria-label="Photograph of an open silver laptop whose screen shows a wooden bookshelf filled with colorful books">
      <defs>
        <linearGradient id="screenTone" x1="0" y1="0" x2="1" y2="1">
          <stop offset="0" stop-color="#c99a5e"/>
          <stop offset="1" stop-color="#9a6a38"/>
        </linearGradient>
        <linearGradient id="baseTone" x1="0" y1="0" x2="0" y2="1">
          <stop offset="0" stop-color="#d8dadf"/>
          <stop offset="1" stop-color="#a9adb4"/>
        </linearGradient>
      </defs>
      <rect x="46" y="0" width="430" height="278" rx="10" fill="url(#screenTone)"/>
      <polygon points="46,278 476,278 537,398 0,398" fill="url(#baseTone)"/>
    </svg>

    <h1 class="title">
      <span class="title-line title-line--top">MAPPING</span>
      <span class="title-line title-line--accent">SCHOOL</span>
      <span class="title-line title-line--bottom">OPTIONS</span>
    </h1>

    <section class="subtitle-band">
      <p class="subtitle">
        <span class="subtitle-line subtitle-line--one">A Handbook for Reading Campus</span>
        <span class="subtitle-line subtitle-line--two">Pages to Spend Little</span>
        <span class="subtitle-line subtitle-line--three">on a Stronger Degree</span>
      </p>
    </section>
  </main>
</body>
</html>
```